Signage. Will be for store front. Building is on a corner lot. Lots of traffic.

Opening a new location for our landscape business with a garden store (boutique theme) which will have big pottery pots, house plants, ferns and orchids for sale.

And on the side lot of the store we will have bigger bulk items(contractors theme) landscape plants, sod, mulch, soil, rock for sale.

Sign is about 8’x6’

Target Market(s)

Home owners
Landscapers
Builders

Industry/Entity Type

Landscaping

Font styles to use
Sans Serif

Colors
9bcb3c

Requirements
Must have
• “ Installation and Delivery” is a big deal to let people know we do that
Nice to have
• Added a first rendition idea but don’t love it
Added a file with some words to play with
Need help with the words
Should not have
• ?

```html
<!DOCTYPE html>
<html lang="en">
<head>
<meta charset="UTF-8">
<title>Briarwood Landscapes – Storefront Sign</title>
<link rel="stylesheet" href="https://fonts.googleapis.com/css2?family=Dancing+Script:wght@700&family=Oswald:wght@500;600&display=swap">
<style>
  :root {
    --page-bg: #e7ecef;
    --sign-white: #f7f7f6;
    --sign-grey: #e7e8e8;
    --olive: #7a9150;
    --olive-dark: #5f7540;
    --ink: #262626;
    --rule: #6f8748;
  }
  * { box-sizing: border-box; margin: 0; padding: 0; }
  html, body {
    width: 1200px;
    height: 900px;
    overflow: hidden;
    background: var(--page-bg);
  }
  .sign {
    position: absolute;
    left: 100px;
    top: 75px;
    width: 1000px;
    height: 750px;
    background: var(--sign-white);
    box-shadow: 0 6px 22px rgba(0,0,0,0.12);
    overflow: hidden;
  }
  .sign__brand-zone {
    position: absolute;
    left: 0; top: 0;
    width: 100%; height: 290px;
    background: var(--sign-white);
  }
  .sign__service-zone {
    position: absolute;
    left: 0; top: 290px;
    width: 100%; height: 290px;
    background: var(--sign-grey);
  }
  .sign__frame {
    position: absolute;
    left: 18px; top: 18px;
    width: 964px; height: 562px;
    border: 3px solid var(--rule);
    border-bottom: none;
  }
  .brand {
    position: absolute;
    left: 0; top: 62px;
    width: 100%;
    display: flex;
    align-items: center;
    justify-content: center;
    gap: 34px;
  }
  .brand__name {
    font-family: "Oswald", sans-serif;
    font-weight: 600;
    color: var(--olive-dark);
    font-size: 74px;
    line-height: 1.0;
    letter-spacing: 6px;
    text-transform: uppercase;
  }
  .brand__dot {
    width: 70px; height: 70px;
    border-radius: 50%;
    background: var(--olive);
    flex: none;
  }
  .services {
    position: absolute;
    left: 0; top: 318px;
    width: 100%;
    text-align: center;
    font-family: "Oswald", sans-serif;
    font-weight: 500;
    color: var(--ink);
    font-size: 58px;
    line-height: 1.2;
    text-transform: uppercase;
  }
  .services__sep {
    display: inline-block;
    width: 3px; height: 0.8em;
    background: var(--ink);
    margin: 0 22px;
    vertical-align: -0.05em;
  }
  .welcome {
    position: absolute;
    left: 0; top: 482px;
    width: 100%;
    text-align: center;
    font-family: "Dancing Script", cursive;
    font-weight: 700;
    color: var(--olive);
    font-size: 74px;
    line-height: 1;
  }
  .offer-band {
    position: absolute;
    left: 0; bottom: 0;
    width: 100%; height: 170px;
    background: var(--olive);
    display: flex;
    align-items: center;
    justify-content: center;
  }
  .offer-band__text {
    font-family: "Oswald", sans-serif;
    font-weight: 600;
    color: #ffffff;
    font-size: 54px;
    line-height: 1;
    letter-spacing: 1px;
    text-transform: uppercase;
    text-align: center;
    white-space: nowrap;
  }
</style>
</head>
<body>
  <section class="sign">
    <div class="sign__brand-zone"></div>
    <div class="sign__service-zone"></div>
    <div class="sign__frame"></div>

    <div class="brand">
      <h1 class="brand__name">Briarwood<br>Landscapes</h1>
      <span class="brand__dot"></span>
    </div>

    <p class="services">
      Sod<span class="services__sep"></span>Landscape Supply<br>
      Lawn<span class="services__sep"></span>Garden<span class="services__sep"></span>Nursery
    </p>

    <p class="welcome">Public Welcome!</p>

    <div class="offer-band">
      <p class="offer-band__text">Installation and Delivery Available</p>
    </div>
  </section>
</body>
</html>
```